Property developer, money partner needs business card design using logo concept provided

Our company develops residential properties, does money lends for joint ventures in property deals and finds property deals for other money partners. We have provided a basic logo for you to work from. Any graphic or logo design on the card is to communicate development and finance collaboration. Color choice is not so important for us, but color choice does need to reflect professionalism.

```html
<!DOCTYPE html>
<html lang="en">
<head>
<meta charset="utf-8">
<title>Brightfield Property Solutions – Business Card</title>
<link rel="stylesheet" href="https://fonts.googleapis.com/css2?family=Lato:wght@400;700;900&display=swap">
<style>
  :root {
    --stage: #2c2c2e;
    --card: #ffffff;
    --brand-blue: #0b62b0;
    --deep-blue: #0a3f8f;
    --accent-red: #9b1b1f;
    --ink: #1e1e1e;
    --rule-grey: #8a8a8a;
  }
  * { box-sizing: border-box; margin: 0; padding: 0; }
  html, body {
    width: 1200px; height: 875px; overflow: hidden;
    background: var(--stage);
    font-family: "Lato", sans-serif;
  }
  .stage {
    position: relative; width: 1200px; height: 875px;
    display: flex; align-items: center; justify-content: center; gap: 40px;
  }
  .card {
    position: relative; width: 540px; height: 310px;
    background: var(--card); border-radius: 26px; overflow: hidden;
    box-shadow: 0 14px 30px rgba(0,0,0,.45);
  }

  /* Front face */
  .card-front { display: flex; align-items: center; padding-left: 56px; gap: 34px; }
  .brand-mark {
    width: 120px; height: 120px; border-radius: 50%;
    background: linear-gradient(145deg, #1a7fd0, var(--deep-blue));
    flex-shrink: 0;
  }
  .brand-name {
    font-weight: 900; font-size: 34px; letter-spacing: 6px; color: var(--ink);
  }
  .brand-tagline { font-size: 19px; letter-spacing: 3px; color: var(--ink); margin-top: 6px; }
  .brand-acn { font-size: 12px; letter-spacing: 3px; color: var(--ink); margin-top: 8px; }

  /* Info face */
  .card-info { padding: 40px 0 0 38px; }
  .holder-name {
    font-weight: 900; font-size: 30px; color: var(--brand-blue); letter-spacing: .5px;
  }
  .holder-title { font-size: 16px; color: var(--accent-red); margin-top: 2px; }
  .title-rule { width: 50px; height: 4px; background: var(--rule-grey); margin-top: 10px; }
  .contact-list { list-style: none; margin-top: 20px; font-size: 14px; color: var(--ink); line-height: 1.3; }
  .contact-list li { display: flex; align-items: flex-start; gap: 10px; margin-bottom: 3px; }
  .contact-list svg { width: 13px; height: 13px; fill: var(--brand-blue); flex-shrink: 0; margin-top: 2px; }
  .company-line { color: var(--brand-blue); font-weight: 700; }
  .info-emblem {
    position: absolute; right: -30px; top: 50px; width: 250px; height: 250px;
    border-radius: 50%; background: linear-gradient(145deg, #1a7fd0, var(--deep-blue));
  }
</style>
</head>
<body>
<main class="stage">
  <section class="card card-front" aria-label="Card front">
    <div class="brand-mark" aria-hidden="true"></div>
    <div class="brand-block">
      <div class="brand-name">BRIGHTFIELD</div>
      <div class="brand-tagline">Property Solutions</div>
      <div class="brand-acn">A.C.N 318 204 956</div>
    </div>
  </section>

  <section class="card card-info" aria-label="Card back">
    <div class="info-emblem" aria-hidden="true"></div>
    <h1 class="holder-name">DANIEL HART</h1>
    <p class="holder-title">Founder &amp; CEO</p>
    <div class="title-rule"></div>
    <ul class="contact-list">
      <li>
        <svg viewBox="0 0 24 24"><path d="M12 2a7 7 0 0 0-7 7c0 5 7 13 7 13s7-8 7-13a7 7 0 0 0-7-7zm0 9.5A2.5 2.5 0 1 1 12 6a2.5 2.5 0 0 1 0 5.5z"/></svg>
        <span><span class="company-line">Brightfield Property Solutions</span><br>Your Address, City<br>State, Country, Zip 1235</span>
      </li>
      <li>
        <svg viewBox="0 0 24 24"><path d="M6.6 10.8a15 15 0 0 0 6.6 6.6l2.2-2.2a1 1 0 0 1 1-.25 11.4 11.4 0 0 0 3.6.57 1 1 0 0 1 1 1V20a1 1 0 0 1-1 1A17 17 0 0 1 3 4a1 1 0 0 1 1-1h3.5a1 1 0 0 1 1 1c0 1.25.2 2.45.57 3.57a1 1 0 0 1-.25 1z"/></svg>
        <span>(555) 210-4471</span>
      </li>
      <li>
        <svg viewBox="0 0 24 24"><path d="M7 1h10a2 2 0 0 1 2 2v18a2 2 0 0 1-2 2H7a2 2 0 0 1-2-2V3a2 2 0 0 1 2-2zm0 3v14h10V4zm5 15.5a1 1 0 1 0 0 2 1 1 0 0 0 0-2z"/></svg>
        <span>(555) 318-9026</span>
      </li>
      <li>
        <svg viewBox="0 0 24 24"><path d="M6 2h12v5H6zM4 8h16a2 2 0 0 1 2 2v7h-4v5H6v-5H2v-7a2 2 0 0 1 2-2zm4 8v4h8v-4z"/></svg>
        <span>(555) 742-1158</span>
      </li>
      <li>
        <svg viewBox="0 0 24 24"><path d="M2 5h20v14H2zm2 2v.5l8 5 8-5V7z"/></svg>
        <span>office@brightfieldprop.com</span>
      </li>
      <li>
        <svg viewBox="0 0 24 24"><path d="M12 2a10 10 0 1 0 0 20 10 10 0 0 0 0-20zm6.9 9h-3a15 15 0 0 0-1.3-5.6A8 8 0 0 1 18.9 11zM12 4c.9 1.2 1.8 3.6 1.9 7h-3.8C10.2 7.6 11.1 5.2 12 4zM9.4 5.4A15 15 0 0 0 8.1 11h-3a8 8 0 0 1 4.3-5.6zM5.1 13h3a15 15 0 0 0 1.3 5.6A8 8 0 0 1 5.1 13zm6.9 7c-.9-1.2-1.8-3.6-1.9-7h3.8c-.1 3.4-1 5.8-1.9 7zm2.6-1.4a15 15 0 0 0 1.3-5.6h3a8 8 0 0 1-4.3 5.6z"/></svg>
        <span>www.brightfieldprop.com</span>
      </li>
    </ul>
  </section>
</main>
</body>
</html>
```